Dietitian/Nutritionist seeks trifold marketing brochure

We need a trifold brochure for marketing to patients within a doctors surgery. This will be a source of information for prospective patients, what they can expect and how to contact us. The brochure needs to have some key information such as a brief description of the services available, fees, locations of clinics and contact information. Our current brochure has been uploaded which has the information you need to complete this project. The files you provide will allow us to edit the information at a later date as pricing and services change.

Target Market(s)

Patients who have been referred to see a dietitian/nutritionist and people who are considering seeing a dietitian/nutritionist but haven't decided

Industry/Entity Type

Dietician

Font styles to use
Serif

Colors

Designer to choose colors to be used in the design.

Requirements
Must have
• My logo
• Verified clinical mealwise logo
• My website address and contact details
• Most of the information that is in my current brochure
• Locations/names of the four clinics
Nice to have
• Images that promote cooking, health and wellbeing

```html
<!DOCTYPE html>
<html lang="en">
<head>
<meta charset="utf-8">
<title>Tamarind Nutrition &amp; Dietetics – Inside Spread</title>
<link href="https://fonts.googleapis.com/css2?family=Arimo:wght@400;700&family=PT+Sans:wght@400;700&display=swap" rel="stylesheet">
<style>
:root{
  --blue:#1a4a9c;
  --blue-deep:#113a86;
  --blue-bright:#1b9ad6;
  --blue-link:#7cc8f5;
  --green:#a7cc22;
  --green-text:#7dbb2a;
  --green-ring:#d8ec6a;
  --navy:#123f8c;
  --ink:#1d1d1d;
  --paper:#f3f4f6;
  --orange:#f26b21;
  --page:#e9e9e9;
}
*{box-sizing:border-box;margin:0;padding:0}
html,body{width:1200px;height:1000px;overflow:hidden;background:var(--page)}
.spread{position:absolute;left:57px;top:32px;width:1088px;height:846px;background:var(--paper);overflow:hidden;font-family:"Arimo",Arial,sans-serif;box-shadow:0 2px 8px rgba(0,0,0,.15)}
.backdrop{position:absolute;inset:0}
.intro{position:absolute;left:44px;top:40px;width:664px;color:#fff;font-size:14.6px;line-height:20.8px}
.intro p+p{margin-top:20px}
.intro .lead{color:var(--blue-link)}
.photo{position:absolute}
.photo-dietitian{left:10px;top:360px;width:400px;height:470px;background:radial-gradient(ellipse at 50% 45%,#e4dcd6 0%,#d9d6d4 40%,rgba(243,244,246,0) 72%)}
.photo-fruit{left:425px;top:292px;width:240px;height:150px;border-radius:50% 50% 45% 45%/40% 40% 60% 60%;background:radial-gradient(ellipse at 50% 40%,#e8553a 0%,#d9a23a 40%,#8fb04a 65%,rgba(220,230,240,.6) 100%)}
.photo-circle{left:782px;top:467px;width:256px;height:256px;border-radius:50%;border:6px solid var(--green-ring);background:radial-gradient(circle at 50% 40%,#e9cbb3 0%,#c98f6f 50%,#8a5a44 100%)}
.bar{position:absolute;height:25px;background:var(--navy);border-radius:3px;color:#fff;font-family:"PT Sans",sans-serif;font-size:20px;line-height:25px;padding-left:8px}
.fees-bar{left:752px;top:36px;width:293px}
.locations-bar{left:392px;top:520px;width:292px}
.fees{position:absolute;left:756px;top:74px;width:290px;font-size:14.4px;line-height:18.6px;color:var(--ink)}
.fees h3{font-family:"PT Sans",sans-serif;font-weight:400;font-size:15px;color:var(--navy);line-height:18.6px}
.fees p{text-align:justify}
.fees .block{margin-bottom:18px}
.rate{display:grid;grid-template-columns:171px 68px auto}
.rate span:nth-child(n+2){color:var(--navy)}
.locations{position:absolute;left:408px;top:552px;width:260px;text-align:center;list-style:none}
.locations li{padding:2px 0 5px;border-bottom:1px dotted #555;margin-bottom:7px}
.locations li:last-child{border-bottom:none}
.locations strong{display:block;font-family:"PT Sans",sans-serif;font-weight:700;font-size:17px;color:var(--green-text);text-transform:uppercase;line-height:20px}
.locations span{font-size:14.4px;color:var(--ink)}
.badge{position:absolute;left:484px;top:760px;width:92px;height:43px;background:var(--orange);border-radius:2px}
.brand{position:absolute;display:flex;align-items:center;gap:8px;font-family:"PT Sans",sans-serif;font-size:22px;color:var(--navy);line-height:1}
.brand i{display:block;width:44px;height:44px;border-radius:50%;background:var(--navy)}
.brand-left{left:88px;top:750px}
.brand-right{left:791px;top:735px}
</style>
</head>
<body>
<main class="spread">
  <svg class="backdrop" viewBox="0 0 1088 846" width="1088" height="846" aria-hidden="true">
    <defs>
      <linearGradient id="blueFill" x1="0" y1="0" x2="1" y2="1">
        <stop offset="0" stop-color="#2058ab"/>
        <stop offset="1" stop-color="#113a86"/>
      </linearGradient>
    </defs>
    <path d="M0 0H730V585C690 500 620 385 480 352C330 322 180 392 0 452Z" fill="url(#blueFill)"/>
    <path d="M0 452C180 392 330 322 480 352C620 385 690 500 730 585" fill="none" stroke="#1b9ad6" stroke-width="14"/>
    <path d="M730 0H1088V705C1000 725 900 705 820 655C780 630 752 605 730 585Z" fill="#a7cc22"/>
  </svg>

  <section class="intro">
    <p><span class="lead">Verified Clinical Mealwise (VCMs)</span> are university trained experts in food and nutrition, they are able to translate the latest scientific evidence into sensible and practical advice. Dietitians differ from nutritionists as they have specific training in clinical environments such as hospitals. This training allows a dietitian to interpret blood tests, understand any food and medication interactions, and communicate with other health professionals involved in your care.</p>
    <p><span class="lead">Seeing a dietitian for the first time</span> involves working with you to develop strategies and goals to improve your health. Follow up visits are recommended to monitor your progress and may include more measurements and new strategies to help YOU realise your goals. Every person is unique and I can provide motivation, support and advice to suit your individual circumstances and lifestyle.</p>
  </section>

  <div class="photo photo-fruit" role="img" aria-label="Glass bowl of fresh fruit salad with berries, kiwi and melon"></div>
  <div class="photo photo-dietitian" role="img" aria-label="Dietitian in a white coat holding a green apple"></div>
  <div class="photo photo-circle" role="img" aria-label="Smiling woman eating a strawberry"></div>

  <h2 class="bar fees-bar">Fees</h2>
  <section class="fees">
    <div class="block">
      <h3>Chronic Disease Management Plans</h3>
      <p>If your Doctor has referred you with a Chronic Disease Management Plan to assist in the ongoing management of your health condition you are eligible for a rebate of $52.95 from HealthCover.</p>
    </div>
    <div class="block">
      <h3>All Fees are payable on the day</h3>
      <h3>Private Patients</h3>
      <div class="rate"><span>Initial Consultation</span><span>(60mins)</span><span>$120</span></div>
      <div class="rate"><span>Follow up Consultation</span><span>(30mins)</span><span>$65</span></div>
    </div>
    <div class="block">
      <h3>Private Health Funds</h3>
      <p>Rebates are available through most private health funds but rates vary depending on your level of cover. Check with your fund directly to find out more.</p>
    </div>
    <p>Payment is required on the day of your consultation. Either by cash, credit card or PayTap</p>
  </section>

  <h2 class="bar locations-bar">Locations</h2>
  <ul class="locations">
    <li><strong>Ashgrove Medical Centre</strong><span>Hillview - Fridays</span></li>
    <li><strong>Kenmore Medical</strong><span>Wednesdays</span></li>
    <li><strong>East Ridge Health Lakeside</strong><span>Thursdays</span></li>
    <li><strong>Fernvale Doctors Surgery</strong><span>Approximately every 4 weeks</span></li>
  </ul>

  <div class="badge" role="img" aria-label="Verified clinical mealwise membership badge"></div>

  <div class="brand brand-left"><i></i><span>Tamarind Nutrition &amp; Dietetics</span></div>
  <div class="brand brand-right"><i></i><span>Tamarind Nutrition &amp; Dietetics</span></div>
</main>
</body>
</html>
```